Power Point Template Design for Consulting Company
Verdant Ridge Inc.
Helping Clients Achieve Explosive Sales
Need a slide master incorporating existing logo for all regular Power Point slide layout types (title, title and content, section header, two content, comparison, title only, blank, content with caption, picture with caption)
Corporate client presentations and professional association speaking engagements
Using Power Point 2007, Windows 7.0 O/S.
Not overpowering, prefer clean white backgrounds for better projection and printing results. Verdant Ridge Inc. Logo was designed on a previous project so all files available.
logo files in all formats
business card for reference and consistency
business letterhead for reference and consistency
business stationary coor and font for reference and consistency

```html
<!DOCTYPE html>
<html lang="en">
<head>
<meta charset="utf-8">
<title>Verdant Ridge Inc. – Title Slide</title>
<link rel="stylesheet" href="https://fonts.googleapis.com/css2?family=Michroma&family=Arimo&family=Open+Sans&display=swap">
<style>
  :root {
    --blue-deep: #0b3c86;
    --blue-mid: #0a66bd;
    --blue-glow: #12a6e6;
    --white: #ffffff;
    --band-light: #eeeeee;
    --band-dark: #8e8e8e;
    --link-blue: #1a5fb0;
  }
  html, body {
    margin: 0;
    width: 1200px;
    height: 915px;
    overflow: hidden;
    background: #ffffff;
  }
  .slide {
    position: relative;
    width: 1200px;
    height: 915px;
    overflow: hidden;
    font-family: "Arimo", Arial, sans-serif;
  }
  .stage {
    position: absolute;
    left: 0; top: 0;
    width: 1200px; height: 818px;
    background: radial-gradient(ellipse 62% 70% at 52% 68%, var(--blue-glow) 0%, var(--blue-mid) 48%, var(--blue-deep) 100%);
  }
  .rays {
    position: absolute;
    left: 0; top: 0;
    width: 1200px; height: 818px;
  }
  .brand {
    position: absolute;
    left: 57px; top: 67px;
  }
  .brand-square {
    position: absolute;
    left: 167px; top: 0;
    width: 140px; height: 140px;
    background: var(--white);
    border-radius: 10px;
  }
  .brand-name {
    position: absolute;
    left: 0; top: 168px;
    margin: 0;
    white-space: nowrap;
    font-family: "Michroma", sans-serif;
    font-size: 38px;
    font-weight: 400;
    color: var(--white);
    letter-spacing: 1px;
  }
  .placeholder {
    position: absolute;
    box-sizing: border-box;
    border: 2px dashed rgba(255,255,255,0.8);
    display: flex;
    align-items: center;
    justify-content: center;
    color: var(--white);
  }
  .placeholder-title {
    left: 200px; top: 336px;
    width: 801px; height: 209px;
    font-size: 48px;
  }
  .placeholder-subtitle {
    left: 292px; top: 573px;
    width: 623px; height: 209px;
    font-size: 40px;
  }
  .divider-band {
    position: absolute;
    left: 0; top: 818px;
    width: 1200px; height: 24px;
    background: linear-gradient(90deg, var(--band-dark) 0%, var(--band-light) 50%, var(--band-dark) 100%);
  }
  .footer {
    position: absolute;
    left: 0; top: 842px;
    width: 1200px; height: 73px;
    background: var(--white);
  }
  .footer-url {
    position: absolute;
    left: 30px; top: 12px;
    margin: 0;
    font-family: "Open Sans", Arial, sans-serif;
    font-size: 36px;
    color: var(--link-blue);
  }
</style>
</head>
<body>
  <main class="slide">
    <div class="stage">
      <svg class="rays" viewBox="0 0 1200 818" aria-hidden="true">
        <g fill="#ffffff">
          <polygon points="640,690 880,0 1010,0" opacity="0.16"/>
          <polygon points="640,690 1060,0 1150,0" opacity="0.22"/>
          <polygon points="640,690 1200,90 1200,210" opacity="0.2"/>
          <polygon points="640,690 1200,300 1200,400" opacity="0.16"/>
          <polygon points="640,690 1200,480 1200,540" opacity="0.1"/>
        </g>
      </svg>

      <div class="brand">
        <div class="brand-square"></div>
        <h1 class="brand-name">Verdant Ridge Inc.</h1>
      </div>

      <div class="placeholder placeholder-title">Click to add title</div>
      <div class="placeholder placeholder-subtitle">Click to add subtitle</div>
    </div>

    <div class="divider-band"></div>
    <footer class="footer">
      <p class="footer-url">verdantridge.com</p>
    </footer>
  </main>
</body>
</html>
```